Lawn mowing business card design

We need a business card design for our lawn mowing and gardening business which is located in the Northern Beaches of Sydney. Our business name is Meadowline Turf and our logo is predominantly green and yellow in color. Please see our website at www.meadowlineturf.com.au for design ideas. The business targets young professionals and older clientele. As such the font should be easy to read, but I also want the business card to be colorful and stand out.

Target Market(s)

young professionals

Industry/Entity Type

Lawn Care

Contact Information for Business Card

Meadowline Turf, Gareth Pellow, 0478559201, www.meadowlineturf.com.au, email: meadowlineturf@mailbox-example.com

Font styles to use
Serif

Colors
9bcb3b
fbed22

Requirements
Must have
• Must include the details listed above. Must include the attached logo.
Nice to have
• Logo attached with two copies. The logo without any writing is high quality, please feel free to be creative with the text stating our business name "Meadowline Turf" using this file.

```html
<!DOCTYPE html>
<html lang="en">
<head>
<meta charset="utf-8">
<title>Meadowline Turf – Business Card</title>
<link href="https://fonts.googleapis.com/css2?family=Merriweather:wght@400;700&display=swap" rel="stylesheet">
<style>
  :root {
    --lawn-green: #9bcb3b;
    --deep-green: #6fae2a;
    --sun-yellow: #fbed22;
    --card-yellow: #f5ed5c;
    --ink: #1f2a1a;
    --line-dark: #2f4a1e;
    --paper: #ffffff;
    --backdrop: #ecebe6;
  }
  * { margin: 0; padding: 0; box-sizing: border-box; }
  html, body { width: 1200px; height: 891px; overflow: hidden; background: var(--backdrop); }
  body {
    font-family: "Merriweather", Georgia, serif;
    color: var(--ink);
    display: flex;
    flex-direction: column;
    align-items: center;
    justify-content: center;
    gap: 40px;
  }
  .card {
    position: relative;
    width: 700px;
    height: 400px;
    overflow: hidden;
    box-shadow: 0 6px 18px rgba(0,0,0,0.18);
  }
  .card-art { position: absolute; inset: 0; }

  /* front */
  .card-front { background: var(--paper); }
  .brand-mark {
    position: absolute;
    left: 0; right: 0; top: 150px;
    display: flex;
    align-items: center;
    justify-content: center;
    gap: 16px;
  }
  .brand-square { width: 34px; height: 34px; background: var(--deep-green); }
  .brand-name {
    font-size: 36px;
    font-weight: 700;
    color: var(--deep-green);
    letter-spacing: 0.5px;
  }

  /* back */
  .card-back { background: var(--card-yellow); }
  .holder-name { position: absolute; left: 70px; top: 120px; font-size: 22px; }
  .business-name { position: absolute; right: 40px; top: 100px; font-size: 20px; }
  .divider { position: absolute; left: 300px; top: 180px; width: 1px; height: 90px; background: var(--lawn-green); }
  .contact-list { position: absolute; left: 330px; top: 190px; list-style: none; font-size: 18px; line-height: 1.9; }
  .contact-list li, .web { display: flex; align-items: center; gap: 12px; }
  .contact-list svg, .web svg { flex: none; }
  .web { position: absolute; left: 40px; top: 290px; font-size: 16px; }
</style>
</head>
<body>

  <section class="card card-front" aria-label="Card front">
    <svg class="card-art" viewBox="0 0 700 400" width="700" height="400">
      <defs>
        <linearGradient id="bandTop" x1="0" y1="0" x2="0" y2="1">
          <stop offset="0" stop-color="#9bcb3b"/>
          <stop offset="0.6" stop-color="#c9dd32"/>
          <stop offset="1" stop-color="#fbed22"/>
        </linearGradient>
        <linearGradient id="bandBottom" x1="0" y1="0" x2="0" y2="1">
          <stop offset="0" stop-color="#fbed22"/>
          <stop offset="0.4" stop-color="#c9dd32"/>
          <stop offset="1" stop-color="#9bcb3b"/>
        </linearGradient>
      </defs>
      <rect x="0" y="0" width="700" height="75" fill="url(#bandTop)"/>
      <polyline points="0,38 560,38 610,55 700,55" fill="none" stroke="#2f4a1e" stroke-width="2.5"/>
      <rect x="0" y="310" width="700" height="90" fill="url(#bandBottom)"/>
      <polyline points="0,345 90,345 140,370 700,370" fill="none" stroke="#2f4a1e" stroke-width="2.5"/>
    </svg>
    <div class="brand-mark">
      <span class="brand-square"></span>
      <span class="brand-name">Meadowline Turf</span>
    </div>
  </section>

  <section class="card card-back" aria-label="Card back">
    <svg class="card-art" viewBox="0 0 700 400" width="700" height="400">
      <polyline points="0,50 270,50 320,80 700,80" fill="none" stroke="#9bcb3b" stroke-width="3"/>
      <polyline points="0,335 380,335 430,365 700,365" fill="none" stroke="#9bcb3b" stroke-width="3"/>
    </svg>
    <p class="holder-name">Gareth Pellow</p>
    <p class="business-name">Meadowline Turf</p>
    <span class="divider"></span>
    <ul class="contact-list">
      <li>
        <svg width="16" height="16" viewBox="0 0 16 16" aria-hidden="true"><path d="M4 1 L6 1 L7 5 L5 6 Q6 9.5 9 11 L10 9 L14 10 L14 12 Q13 15 10 14 Q3 11 2 4 Q2 1.5 4 1Z" fill="#1f2a1a"/></svg>
        0478559201
      </li>
      <li>
        <svg width="18" height="14" viewBox="0 0 18 14" aria-hidden="true"><rect x="1" y="1" width="16" height="12" fill="none" stroke="#1f2a1a" stroke-width="1.6"/><polyline points="1,1 9,8 17,1" fill="none" stroke="#1f2a1a" stroke-width="1.6"/></svg>
        meadowlineturf@mailbox-example.com
      </li>
    </ul>
    <p class="web">
      <svg width="18" height="18" viewBox="0 0 18 18" aria-hidden="true"><circle cx="9" cy="9" r="7.5" fill="none" stroke="#1f2a1a" stroke-width="1.5"/><ellipse cx="9" cy="9" rx="3.2" ry="7.5" fill="none" stroke="#1f2a1a" stroke-width="1.2"/><line x1="1.5" y1="9" x2="16.5" y2="9" stroke="#1f2a1a" stroke-width="1.2"/></svg>
      www.meadowlineturf.com.au
    </p>
  </section>

</body>
</html>
```